KTR Business Cards

We require business cards for our business. We would like a matte black back to the card, with our logo centred in the middle. The front side of the card is open to design.

Target Market(s)

Clients looking for legal services (professional)

Industry/Entity Type

Legal

Contact Information for Business Card

Dario Velkenor
Partner
Mobile: 0471 386 524
Email: dario@ktrlaw.co
Website: www.ktrlaw.co
Level 3, 118 Pembury Street
Sydney NSW 2000

Font styles to use
Other font styles liked:
• Avenir

Colors
f04a50
ffffff
1b1b1b

Requirements
Must have
• Black back with logo included in the centre of the card.
• Our font is Avenir.

```html
<!DOCTYPE html>
<html lang="en">
<head>
<meta charset="utf-8">
<title>Keller Tarnow Ryde – Business Cards</title>
<link rel="stylesheet" href="https://fonts.googleapis.com/css2?family=Roboto:wght@400;500&display=swap">
<style>
  :root {
    --brand-red: #d31f47;
    --ink: #1b1b1b;
    --card-black: #231f20;
    --paper: #ffffff;
    --muted: #555555;
    --backdrop: #e4e4e4;
  }
  * { margin: 0; padding: 0; box-sizing: border-box; }
  html, body {
    width: 1125px; height: 1200px; overflow: hidden;
    background: var(--backdrop);
    font-family: "Roboto", Arial, sans-serif;
  }
  .card {
    position: absolute; left: 166px; width: 800px; height: 457px; overflow: hidden;
  }
  .card--front { top: 103px; background: var(--paper); }
  .card--back { top: 619px; background: var(--card-black); }

  .firm-name {
    position: absolute; display: flex; align-items: center; gap: 18px;
  }
  .firm-name__mark { width: 46px; height: 46px; background: var(--brand-red); flex: none; }
  .firm-name__text {
    font-weight: 500; text-transform: uppercase; line-height: 30px; letter-spacing: 0.5px;
  }
  .card--front .firm-name { right: 40px; top: 66px; }
  .card--front .firm-name__text { font-size: 28px; color: var(--ink); }

  .person { position: absolute; left: 50px; top: 256px; }
  .person__name { font-size: 30px; font-weight: 500; color: var(--brand-red); line-height: 34px; }
  .person__role { font-size: 19px; font-weight: 500; color: var(--ink); line-height: 24px; }

  .divider { position: absolute; left: 50px; top: 324px; width: 704px; height: 1px; background: #444; }

  .contact { position: absolute; left: 48px; top: 346px; list-style: none; }
  .contact__item { display: flex; align-items: center; gap: 12px; font-size: 19px; color: var(--muted); height: 26px; }
  .contact__icon { width: 16px; height: 16px; flex: none; }

  .address {
    position: absolute; right: 40px; top: 347px; text-align: right;
    font-size: 19px; line-height: 25px; color: var(--muted); font-style: normal;
  }

  .footer-bands { position: absolute; left: 0; bottom: 0; width: 800px; height: 41px; }
  .footer-url {
    position: absolute; right: 34px; bottom: 11px; color: var(--paper);
    font-size: 19px; letter-spacing: 6.5px;
  }

  .card--back .firm-name { left: 0; right: 0; top: 170px; justify-content: center; }
  .card--back .firm-name__text { font-size: 34px; line-height: 38px; color: var(--paper); }
  .back-url {
    position: absolute; left: 0; right: 0; top: 386px; text-align: center;
    color: var(--paper); font-size: 17px; letter-spacing: 12px; padding-left: 12px;
  }
</style>
</head>
<body>
  <section class="card card--front">
    <div class="firm-name">
      <span class="firm-name__mark"></span>
      <span class="firm-name__text">Keller<br>Tarnow<br>Ryde</span>
    </div>

    <div class="person">
      <p class="person__name">Dario Velkenor</p>
      <p class="person__role">Partner</p>
    </div>

    <div class="divider"></div>

    <ul class="contact">
      <li class="contact__item">
        <svg class="contact__icon" viewBox="0 0 16 16" aria-hidden="true">
          <rect x="3" y="0.5" width="10" height="15" rx="1.5" fill="none" stroke="var(--brand-red)" stroke-width="1.6"/>
          <rect x="6.5" y="12.2" width="3" height="1.4" fill="var(--brand-red)"/>
        </svg>
        <span>0471 386 524</span>
      </li>
      <li class="contact__item">
        <svg class="contact__icon" viewBox="0 0 16 16" aria-hidden="true">
          <rect x="0.5" y="3" width="15" height="10" fill="var(--brand-red)"/>
          <path d="M1 4 L8 9 L15 4" fill="none" stroke="var(--paper)" stroke-width="1.2"/>
        </svg>
        <span>dario@ktrlaw.co</span>
      </li>
    </ul>

    <address class="address">Level 3, 118 Pembury<br>Street, Sydney NSW 2000</address>

    <svg class="footer-bands" viewBox="0 0 800 41" aria-hidden="true">
      <polygon points="0,21 472,21 464,29 0,29" fill="var(--brand-red)"/>
      <polygon points="0,29 464,29 458,33 0,33" fill="#e9c9d1"/>
      <polygon points="496,0 800,0 800,41 456,41" fill="var(--card-black)"/>
      <rect x="0" y="33" width="460" height="8" fill="var(--card-black)"/>
    </svg>
    <span class="footer-url">www.ktrlaw.co</span>
  </section>

  <section class="card card--back">
    <div class="firm-name">
      <span class="firm-name__mark"></span>
      <span class="firm-name__text">Keller<br>Tarnow<br>Ryde</span>
    </div>
    <p class="back-url">WWW.KTRLAW.CO</p>
  </section>
</body>
</html>
```